Need Bus charter business website,

I am starting a bus charter business in the near future. I am based in Geelong, Victoria in Australia. I will have a 25 or 28 seater bus that will be used to take people on charted trips. Whether they be to birthday parties, weddings, sporting events, corporate events, mystery trips, going down the Great Ocean Road, or anywhere someone wants. As for colour scheme, I'm leaning towards something blue and grey, but open to anything really that catches my eye. I played around with a basic web design program and made a basic site which I uploaded ( www.kelvomtravel.com.au) It has things which I wanted to include such as, services I will provide, trip information, contact form etc.

I don't mind if the layout is completely different to my site as it was only a template that was included in the program I used. I would like the overall design to be relatively fluid, not having to back-track a lot to navigate the site.

```html
<!DOCTYPE html>
<html lang="en">
<head>
<meta charset="utf-8">
<title>Bayline Coach Tours</title>
<link rel="stylesheet" href="https://fonts.googleapis.com/css2?family=Open+Sans:wght@300;400;600;700&display=swap">
<style>
:root{
  --blue:#1a4596;
  --blue-bright:#1f5db8;
  --charcoal:#474747;
  --dark:#2e2e2e;
  --ink:#333333;
  --muted:#6b6b6b;
  --header-bg:#efefef;
  --page-bg:#f2f2f2;
  --card-bg:#e3e3e3;
  --white:#ffffff;
  --forest:#3d5a2b;
  --forest-light:#5f7f3d;
  --coach:#eef0f1;
}
*{box-sizing:border-box;margin:0;padding:0}
html,body{width:671px;height:1200px;overflow:hidden}
body{position:relative;font-family:"Open Sans",Arial,sans-serif;color:var(--ink);background:var(--page-bg)}
.abs{position:absolute}

/* header */
.site-header{left:0;top:0;width:671px;height:63px;background:var(--header-bg)}
.brand{left:60px;top:16px;display:flex;align-items:center;gap:8px;font-size:19px;font-weight:600;color:var(--dark)}
.brand-mark{width:12px;height:12px;background:var(--dark)}
.main-nav{left:289px;top:0;height:63px;display:flex}
.main-nav a{display:block;height:63px;line-height:60px;padding:0 7px;font-size:10px;font-weight:600;color:var(--dark);text-decoration:none}
.main-nav a.active{background:var(--blue);color:var(--white)}

/* hero */
.hero{left:0;top:63px;width:671px;height:299px;border-top:3px solid var(--blue);overflow:hidden}
.hero-photo{position:absolute;inset:0;
  background:
    radial-gradient(ellipse 290px 140px at 310px 130px,var(--coach) 0%,#e2e5e7 55%,rgba(226,229,231,0) 100%),
    linear-gradient(180deg,var(--forest) 0%,var(--forest-light) 55%,#8e9a88 82%,#6d7570 100%)}
.hero-tagline{left:66px;top:124px;font-size:18px;font-weight:600;line-height:21px;color:#2a2a2a;text-align:center;transform:rotate(-4deg);text-transform:uppercase}
.slide-arrow{top:128px}
.slide-dots{left:657px;top:208px;width:3px}
.slide-dots span{display:block;width:3px;height:22px;margin-bottom:4px;background:var(--white)}
.slide-dots span.on{background:var(--blue-bright)}

/* quote form */
.quote-bar{left:55px;top:305px;width:560px;height:57px;background:rgba(40,40,40,.72)}
.quote-tab{left:55px;top:290px;width:175px;height:28px;background:var(--blue);color:var(--white);font-size:12.5px;line-height:27px;padding-left:5px;clip-path:polygon(0 0,100% 0,92% 100%,0 100%)}
.quote-type{left:221px;top:310px;display:flex;gap:20px;font-size:10px;color:var(--white);align-items:center}
.quote-type label{display:flex;align-items:center;gap:7px}
.quote-type i{width:13px;height:13px;border:1.5px solid var(--dark);background:var(--white)}
.quote-type i.solid{border-color:var(--white)}
.field{height:18px;background:var(--white);font-size:8px;color:#888;line-height:18px;padding-left:5px}
.field .req{position:absolute;right:4px;top:0;color:#d22}
.field.select::after{content:"";position:absolute;right:5px;top:7px;border:4px solid transparent;border-top:5px solid #333}
.quote-submit{left:501px;top:336px;width:88px;height:18px;background:var(--blue);color:var(--white);font-size:11px;text-align:center;line-height:18px;font-weight:600}

/* welcome */
.welcome{left:0;top:362px;width:671px;height:42px;background:var(--blue);color:var(--white);text-align:center;font-size:24px;font-weight:300;line-height:42px}
.welcome b{font-weight:400;font-size:26px}

/* services */
.services{left:55px;top:427px;width:560px;display:flex;gap:2px}
.service-card{width:138.5px;height:207px;background:var(--card-bg);border-top:3px solid var(--blue);text-align:center;position:relative}
.service-photo{height:95px}
.service-card h3{font-size:11px;font-weight:400;margin-top:11px;color:var(--dark)}
.service-card p{font-size:6px;line-height:8px;color:var(--muted);margin:11px 10px 0}
.btn-more{position:absolute;left:47px;top:187px;width:43px;height:13px;background:#444;color:var(--white);font-size:7px;line-height:13px}
.btn-more.primary{background:var(--blue)}

/* newsletter */
.newsletter{left:0;top:658px;width:671px;height:87px;background:var(--charcoal)}
.newsletter h2{position:absolute;left:97px;top:33px;font-size:15px;font-weight:400;color:var(--white)}
.newsletter p{position:absolute;left:281px;top:29px;width:160px;font-size:7.5px;line-height:9.5px;font-weight:700;color:var(--white)}
.news-email{left:436px;top:38px;width:121px;height:17px;background:#ebe6e6;font-size:7px;color:#999;line-height:17px;padding-left:6px}
.news-submit{left:557px;top:38px;width:50px;height:17px;background:var(--blue-bright);color:var(--white);font-size:7.5px;text-align:center;line-height:17px}

/* about + video */
.about-card{left:56px;top:766px;width:310px;height:142px;background:#f0f0f0;border:1px solid #d8d8d8}
.about-art{position:absolute;left:0;top:0;width:106px;height:140px;background:linear-gradient(160deg,#f6f1e7 0%,#e8c9a8 45%,#b9423a 75%,#e9e4dc 100%);border-right:1px solid #d0d0d0}
.about-card h2{position:absolute;left:111px;top:5px;font-size:15px;font-weight:400;color:var(--dark)}
.about-card p{position:absolute;left:111px;top:34px;width:193px;font-size:6.3px;line-height:8.3px;color:var(--muted);text-align:justify}
.btn-read{left:259px;top:119px;width:45px;height:14px;background:#9c9c9c;color:var(--white);font-size:6.5px;line-height:14px;text-align:center}
.video{left:385px;top:767px;width:230px;height:141px;background:linear-gradient(180deg,#2a2a2a,#3b3833 60%,#1f1f1f);box-shadow:0 1px 3px rgba(0,0,0,.4)}
.video-bar{position:absolute;left:0;bottom:0;width:230px;height:20px;background:#161616}

/* skyline */
.skyline{left:0;top:908px;width:671px;height:90px;background:linear-gradient(180deg,rgba(138,138,138,0) 0%,rgba(138,138,138,.45) 45%,#8a8a8a 100%)}

/* footer */
.site-footer{left:0;top:998px;width:671px;height:187px;background:var(--charcoal);border-top:3px solid var(--blue)}
.site-footer h4{position:absolute;font-size:10px;font-weight:400;color:var(--white)}
.social span{position:absolute;top:34px;width:20px;height:20px;border-radius:50%;background:#5f5f5f}
.social span.on{background:var(--blue-bright)}
.blog-title{left:72px;top:97px;font-size:7.5px;color:var(--white)}
.blog-date{left:72px;top:108px;font-size:6.5px;color:var(--blue-bright)}
.blog-text{left:72px;top:118px;width:150px;font-size:6.5px;line-height:9px;color:#dcdcdc}
.blog-more{left:72px;top:156px;font-size:6.5px;color:var(--blue-bright)}
.ad-list{left:253px;top:33px;width:147px;list-style:none}
.ad-list li{height:13.5px;border-bottom:1px solid #9a9a9a;font-size:5.8px;line-height:12.5px;color:#dcdcdc;padding-left:2px}
.ad-list li::before{content:"» ";color:#bbb}
.contact-field{left:452px;width:148px;background:#dcdcdc;font-size:6.5px;color:#888;padding:4px 5px}
.contact-submit{left:561px;top:151px;width:39px;height:14px;background:var(--blue);color:var(--white);font-size:6.5px;font-weight:700;text-align:center;line-height:14px}
.bottom-bar{left:0;top:1185px;width:671px;height:15px;background:var(--blue)}
</style>
</head>
<body>

<header class="site-header abs">
  <div class="brand abs"><span class="brand-mark"></span>Bayline Coach Tours</div>
  <nav class="main-nav abs">
    <a class="active" href="#">Home</a>
    <a href="#">About</a>
    <a href="#">Services</a>
    <a href="#">Moving Tips</a>
    <a href="#">Testimonials</a>
    <a href="#">Contact Us</a>
  </nav>
</header>

<section class="hero abs">
  <div class="hero-photo" role="img" aria-label="White charter coach on a road in front of a green forest"></div>
  <div class="hero-tagline abs">When you move with us,<br>it's almost fun</div>
  <svg class="slide-arrow abs" style="left:10px" width="12" height="18" viewBox="0 0 12 18"><path d="M10 2 3 9l7 7" fill="none" stroke="#fff" stroke-width="2"/></svg>
  <svg class="slide-arrow abs" style="left:648px" width="12" height="18" viewBox="0 0 12 18"><path d="M2 2l7 7-7 7" fill="none" stroke="#fff" stroke-width="2"/></svg>
  <div class="slide-dots abs"><span></span><span class="on"></span><span></span></div>
</section>

<div class="quote-bar abs"></div>
<div class="quote-tab abs">GET A FREE QUOTE NOW</div>
<div class="quote-type abs">
  <label><i></i>Residential</label>
  <label><i class="solid"></i>Commercial</label>
</div>
<div class="field abs" style="left:60px;top:336px;width:105px">Name<span class="req">*</span></div>
<div class="field abs" style="left:173px;top:336px;width:105px">Phone #<span class="req">*</span></div>
<div class="field select abs" style="left:286px;top:336px;width:61px">Move From</div>
<div class="field select abs" style="left:355px;top:336px;width:59px">Move To</div>
<div class="field abs" style="left:422px;top:336px;width:61px">Date
  <svg class="abs" style="right:3px;top:3px" width="12" height="12" viewBox="0 0 12 12"><rect x="1" y="2" width="10" height="9" fill="none" stroke="#444"/><path d="M1 5h10M4 1v2M8 1v2M3 7h6M3 9h6" stroke="#444"/></svg>
</div>
<div class="quote-submit abs">SUBMIT</div>

<div class="welcome abs">Welcome to <b>Bayline Coach Tours</b></div>

<section class="services abs">
  <article class="service-card">
    <div class="service-photo" role="img" aria-label="Group of friends celebrating a birthday inside a party bus" style="background:linear-gradient(160deg,#3a2a3a,#b98a8a 55%,#2b2b3b)"></div>
    <h3>Birthday Parties</h3>
    <p>Sorrupti quos dolores et quas molestias excepturi sint occa- ecati cupificia deserunt mollitia animi,</p>
    <div class="btn-more primary">More</div>
  </article>
  <article class="service-card">
    <div class="service-photo" role="img" aria-label="White coach for wedding transport" style="background:linear-gradient(170deg,#4d6f9a,#e6e8ea 55%,#8d8d8d)"></div>
    <h3>Weddings</h3>
    <p>Sorrupti quos dolores et quas molestias excepturi sint occa- ecati cupificia deserunt mollitia animi,</p>
    <div class="btn-more">More</div>
  </article>
  <article class="service-card">
    <div class="service-photo" role="img" aria-label="Silver coach for sporting event trips" style="background:linear-gradient(170deg,#2f2f2f,#b4b2ac 55%,#555)"></div>
    <h3>Sporting Events</h3>
    <p>Sorrupti quos dolores et quas molestias excepturi sint occa- ecati cupificia deserunt mollitia animi,</p>
    <div class="btn-more">More</div>
  </article>
  <article class="service-card">
    <div class="service-photo" role="img" aria-label="Leather seats inside a corporate coach" style="background:linear-gradient(180deg,#d9d9d9,#5a4a44 55%,#2a2523)"></div>
    <h3>Corporate Events</h3>
    <p>Sorrupti quos dolores et quas molestias excepturi sint occa- ecati cupificia deserunt mollitia animi,</p>
    <div class="btn-more">More</div>
  </article>
</section>

<section class="newsletter abs">
  <svg class="abs" style="left:64px;top:31px" width="26" height="24" viewBox="0 0 26 24"><path d="M1 10 25 1l-6 22-7-7-4 6v-8z M12 16 25 1 8 14" fill="none" stroke="#fff" stroke-width="1.5" stroke-linejoin="round"/></svg>
  <h2>Subscribe To Newsletter</h2>
  <p>Lorem ipsum dolor sit amet, consectetur adipisicing elit, sed do eiusmod tempor incididunt ut labore</p>
  <div class="news-email abs">Email</div>
  <div class="news-submit abs">Submit</div>
</section>

<section class="about-card abs">
  <div class="about-art" role="img" aria-label="Cartoon illustration of tourists riding a red double-decker bus"></div>
  <h2>About Us</h2>
  <p>Lorem ipsum dolor sit amet, consect etur adipiscing elit. Integer sit amet erat non turpis interdum facilisis sit amet sit amet turpis sollicitudin.Lorem ipsum dolor sit amet, consect etur adipiscing elit. Integer sit amet erat non turpis interdum facilisis sit amet sit amet turpis sollicitudin.</p>
  <div class="btn-read abs">Read More</div>
</section>

<section class="video abs" role="img" aria-label="Video player showing a passenger looking out of a coach window">
  <svg class="abs" style="left:91px;top:38px" width="50" height="50" viewBox="0 0 50 50"><circle cx="25" cy="25" r="24" fill="rgba(255,255,255,.25)"/><path d="M19 14v22l18-11z" fill="rgba(255,255,255,.8)"/></svg>
  <div class="video-bar">
    <svg width="230" height="20" viewBox="0 0 230 20">
      <path d="M7 6v8l6-4z" fill="#ddd"/>
      <rect x="18" y="9" width="108" height="2" fill="#555"/><rect x="18" y="9" width="40" height="2" fill="#c22"/>
      <text x="131" y="13" font-size="6.5" fill="#eee" font-family="Open Sans,sans-serif">1:26 / 3:22</text>
      <path d="M166 8h2l3-3v10l-3-3h-2z" fill="#ddd"/><rect x="175" y="9" width="14" height="2" fill="#c22"/>
      <path d="M200 6l3 3m-3-3v2m0-2h2M208 14l-3-3m3 3v-2m0 2h-2" stroke="#ddd"/>
      <text x="214" y="13" font-size="7" font-weight="700" fill="#eee" font-family="Open Sans,sans-serif">HD</text>
    </svg>
  </div>
</section>

<div class="skyline abs" role="img" aria-label="Grey city skyline silhouette"></div>

<footer class="site-footer abs">
  <h4 style="left:72px;top:14px">SOCIAL LINKS</h4>
  <div class="social">
    <span class="on" style="left:72px"></span>
    <span style="left:100px"></span>
    <span style="left:127px"></span>
  </div>
  <h4 style="left:72px;top:76px">BLOGS</h4>
  <div class="blog-title abs">Post Title</div>
  <div class="blog-date abs">12 March 2015</div>
  <p class="blog-text abs">Lorem ipsum dolor sit amet, consectetur adipiscing elit. Nunc non diam erat. In fringilla massa ut nisl ullamcorper pellentesque.</p>
  <div class="blog-more abs">Read More</div>

  <h4 style="left:253px;top:14px">ADVERTISE WITH US</h4>
  <ul class="ad-list abs">
    <li>Lorem ipsum dolor sit</li>
    <li>Amet consectetur</li>
    <li>Praesent vel sem id</li>
    <li>Curabitur hendrerit est</li>
    <li>Aliquam eget erat nec sapien</li>
    <li>Cras id augue nunc</li>
    <li>In nec justo non</li>
    <li>Vivamus mollis enim ut</li>
    <li>Curabitur hendrerit est</li>
  </ul>

  <h4 style="left:452px;top:14px">CONTACT US</h4>
  <div class="contact-field abs" style="top:32px;height:17px">Name</div>
  <div class="contact-field abs" style="top:52px;height:17px">Email</div>
  <div class="contact-field abs" style="top:72px;height:63px">Massage</div>
  <div class="contact-submit abs">SUBMIT</div>
</footer>
<div class="bottom-bar abs"></div>

</body>
</html>
```